Spray Foam Company Business Card

We need a business card designed for our spray foam insulation and roof coatings business. We handle residential and commercial projects.
Construction
We would like it to say:
R & K Spray
with these bullet points
-foam insulation
-waterproofing roof system
-water proofing foundation systems
website is rksprayfoaminsulation.example (this was just purchased)
office phone : 630-482-9164
And 3 cards with names on them the names are :
Derek Halvorsen
Curtis Pennington
Rob Stallworth
maybe the bullet points can go on the back?
if you go this website it is another division of our company and you can see the font we use in the R & K. We do not want to use the same half circles that it has just the lettering
www.coatedrightforyears.example

```html
<!DOCTYPE html>
<html lang="en">
<head>
<meta charset="utf-8">
<title>R &amp; K Spray — Business Cards</title>
<link rel="stylesheet" href="https://fonts.googleapis.com/css2?family=Jost:wght@400;600&display=swap">
<style>
  :root {
    --bg: #b9b9bb;
    --ink: #ffffff;
    --blue: #3f5aa8;
    --violet: #4a2a6a;
    --crimson: #7c2d55;
    --red: #b52a2a;
    --orange: #dc4f2a;
    --amber: #e0ab2e;
    --shadow: rgba(0, 0, 0, 0.28);
  }
  * { box-sizing: border-box; margin: 0; padding: 0; }
  html, body { width: 1200px; height: 1000px; overflow: hidden; }
  body {
    background: var(--bg);
    font-family: "Jost", "Futura", sans-serif;
    color: var(--ink);
  }
  .card-sheet {
    position: absolute;
    left: 85px;
    top: 199px;
    display: grid;
    grid-template-columns: 500px 500px;
    grid-template-rows: 286px 286px;
    gap: 30px;
  }
  .card {
    position: relative;
    width: 500px;
    height: 286px;
    background: linear-gradient(90deg,
      var(--blue) 0%, var(--violet) 22%, var(--crimson) 38%,
      var(--red) 52%, var(--orange) 72%, var(--amber) 100%);
    box-shadow: 4px 6px 10px var(--shadow);
  }
  .brand {
    position: absolute;
    font-weight: 600;
    letter-spacing: 0.04em;
    white-space: nowrap;
    line-height: 1;
  }
  .card--front .brand { left: 70px; top: 62px; font-size: 58px; }
  .card--contact .brand { right: 32px; top: 66px; font-size: 40px; }
  .services {
    position: absolute;
    left: 58px;
    top: 158px;
    list-style: none;
    font-size: 19px;
    font-weight: 400;
    line-height: 1.22;
  }
  .services li::before { content: "\2022"; margin-right: 7px; }
  .contact {
    position: absolute;
    left: 30px;
    bottom: 30px;
  }
  .contact__name {
    font-size: 21px;
    font-weight: 600;
    letter-spacing: 0.14em;
    text-transform: uppercase;
    margin: 0 0 4px 28px;
  }
  .contact__line {
    display: flex;
    align-items: center;
    gap: 8px;
    font-size: 18px;
    letter-spacing: 0.06em;
    line-height: 1.4;
  }
  .contact__icon { width: 20px; height: 20px; flex: none; }
</style>
</head>
<body>
  <main class="card-sheet">
    <section class="card card--front">
      <div class="brand">R &amp; K Spray</div>
      <ul class="services">
        <li>foam insulation</li>
        <li>waterproofing roof system</li>
        <li>water proofing foundation systems</li>
      </ul>
    </section>

    <section class="card card--contact">
      <div class="brand">R &amp; K Spray</div>
      <div class="contact">
        <p class="contact__name">Derek Halvorsen</p>
        <p class="contact__line">
          <svg class="contact__icon" viewBox="0 0 24 24"><path fill="#fff" d="M6.6 10.8a15 15 0 0 0 6.6 6.6l2.2-2.2a1 1 0 0 1 1-.25 11.4 11.4 0 0 0 3.6.57 1 1 0 0 1 1 1V20a1 1 0 0 1-1 1A17 17 0 0 1 3 4a1 1 0 0 1 1-1h3.5a1 1 0 0 1 1 1c0 1.25.2 2.45.57 3.57a1 1 0 0 1-.25 1z"/></svg>
          630-482-9164
        </p>
        <p class="contact__line">
          <svg class="contact__icon" viewBox="0 0 24 24"><circle cx="12" cy="12" r="9.5" fill="none" stroke="#fff" stroke-width="2"/><ellipse cx="12" cy="12" rx="4" ry="9.5" fill="none" stroke="#fff" stroke-width="1.6"/><path d="M2.5 12h19M4.5 7h15M4.5 17h15" stroke="#fff" stroke-width="1.4"/></svg>
          rksprayfoaminsulation.example
        </p>
      </div>
    </section>

    <section class="card card--contact">
      <div class="brand">R &amp; K Spray</div>
      <div class="contact">
        <p class="contact__name">Curtis Pennington</p>
        <p class="contact__line">
          <svg class="contact__icon" viewBox="0 0 24 24"><path fill="#fff" d="M6.6 10.8a15 15 0 0 0 6.6 6.6l2.2-2.2a1 1 0 0 1 1-.25 11.4 11.4 0 0 0 3.6.57 1 1 0 0 1 1 1V20a1 1 0 0 1-1 1A17 17 0 0 1 3 4a1 1 0 0 1 1-1h3.5a1 1 0 0 1 1 1c0 1.25.2 2.45.57 3.57a1 1 0 0 1-.25 1z"/></svg>
          630-482-9164
        </p>
        <p class="contact__line">
          <svg class="contact__icon" viewBox="0 0 24 24"><circle cx="12" cy="12" r="9.5" fill="none" stroke="#fff" stroke-width="2"/><ellipse cx="12" cy="12" rx="4" ry="9.5" fill="none" stroke="#fff" stroke-width="1.6"/><path d="M2.5 12h19M4.5 7h15M4.5 17h15" stroke="#fff" stroke-width="1.4"/></svg>
          rksprayfoaminsulation.example
        </p>
      </div>
    </section>

    <section class="card card--contact">
      <div class="brand">R &amp; K Spray</div>
      <div class="contact">
        <p class="contact__name">Rob Stallworth</p>
        <p class="contact__line">
          <svg class="contact__icon" viewBox="0 0 24 24"><path fill="#fff" d="M6.6 10.8a15 15 0 0 0 6.6 6.6l2.2-2.2a1 1 0 0 1 1-.25 11.4 11.4 0 0 0 3.6.57 1 1 0 0 1 1 1V20a1 1 0 0 1-1 1A17 17 0 0 1 3 4a1 1 0 0 1 1-1h3.5a1 1 0 0 1 1 1c0 1.25.2 2.45.57 3.57a1 1 0 0 1-.25 1z"/></svg>
          630-482-9164
        </p>
        <p class="contact__line">
          <svg class="contact__icon" viewBox="0 0 24 24"><circle cx="12" cy="12" r="9.5" fill="none" stroke="#fff" stroke-width="2"/><ellipse cx="12" cy="12" rx="4" ry="9.5" fill="none" stroke="#fff" stroke-width="1.6"/><path d="M2.5 12h19M4.5 7h15M4.5 17h15" stroke="#fff" stroke-width="1.4"/></svg>
          rksprayfoaminsulation.example
        </p>
      </div>
    </section>
  </main>
</body>
</html>
```